Designed the Labels for a bottle of Fellwick Gin

My com nay is The Bramblewood Distilling Company. We make kraft Gins and we our about to launch a new Gin Called Fellwick Gin.

The bottle to be used can be found at the following link...https://www.vessel-depot-example.co.uk/Glass-bottles/Glass-bottles/100ml-glass-bottles/500ml-stoneware-crock-Tall-with-cork-finish-black-mat.html

I would like the front label to say Fellwick Gin with the word Lancashire vertical and Gin Horizontal. A Red Rose is the symbol for Lancashire so this needs to be woven onto the design….it could taken be red rose petals rather that a flower or bud….creatively I'd like it to have a more modern feel.

For the back label I have attached a previous label to illustrate technical information required. The works will change and the new back label may include the Lancashire Rose symbol as used by Marrowdale District Council.

Target Market(s)

UK Retail

Industry/Entity Type

It Company

Requirements
Must have
• A front and back label to fit the bottle described
Nice to have
• Modern and crisp…the bottle is black so that helps catch the eye. The label may be transparent.

```html
<!DOCTYPE html>
<html lang="en">
<head>
<meta charset="utf-8">
<title>Fellwick Gin – Front Label</title>
<link rel="stylesheet" href="https://fonts.googleapis.com/css2?family=Alfa+Slab+One&family=Pathway+Gothic+One&display=swap">
<style>
  :root {
    --backdrop: #ededed;
    --label-black: #141414;
    --ink-white: #ffffff;
    --rose-red: #e0141b;
    --leaf-green: #1f8a3c;
    --band-red: #e3141c;
  }
  * { margin: 0; padding: 0; box-sizing: border-box; }
  html, body {
    width: 877px;
    height: 1200px;
    overflow: hidden;
    background: var(--backdrop);
  }
  .front-label {
    position: absolute;
    left: 128px;
    top: 108px;
    width: 620px;
    height: 985px;
    background: var(--label-black);
    color: var(--ink-white);
  }
  .county-word {
    position: absolute;
    left: 14px;
    top: 14px;
    height: 850px;
    display: flex;
    flex-direction: column;
    justify-content: space-between;
    align-items: center;
    width: 76px;
    font-family: "Alfa Slab One", serif;
    font-size: 82px;
    line-height: 1;
  }
  .rose-art {
    position: absolute;
    left: 128px;
    top: 32px;
    width: 364px;
    height: 578px;
  }
  .product-word {
    position: absolute;
    left: 206px;
    top: 585px;
    font-family: "Alfa Slab One", serif;
    font-size: 200px;
    line-height: 1;
    letter-spacing: -2px;
  }
  .maker-band {
    position: absolute;
    left: 110px;
    top: 806px;
    width: 506px;
    height: 68px;
    background: var(--band-red);
    transform: rotate(-2.2deg);
    display: flex;
    align-items: center;
    justify-content: center;
    font-family: "Pathway Gothic One", sans-serif;
    font-size: 40px;
    white-space: nowrap;
  }
  .spec {
    position: absolute;
    top: 915px;
    font-family: "Pathway Gothic One", sans-serif;
    font-size: 30px;
  }
  .spec-strength { left: 12px; }
  .spec-volume { left: 500px; }
</style>
</head>
<body>
  <main class="front-label">
    <div class="county-word" aria-label="Fellwick">
      <span>F</span><span>e</span><span>l</span><span>l</span><span>w</span><span>i</span><span>c</span><span>k</span>
    </div>

    <svg class="rose-art" viewBox="0 0 364 578" role="img" aria-label="Illustration of a red rose with green leaves">
      <defs>
        <radialGradient id="roseTone" cx="0.5" cy="0.45" r="0.55">
          <stop offset="0" stop-color="#e0141b"/>
          <stop offset="0.6" stop-color="#c8121a"/>
          <stop offset="1" stop-color="#1f8a3c" stop-opacity="0.55"/>
        </radialGradient>
      </defs>
      <rect x="0" y="0" width="364" height="578" fill="url(#roseTone)" opacity="0.9"/>
    </svg>

    <div class="product-word">Gin</div>

    <div class="maker-band">The Bramblewood Distilling Company</div>

    <div class="spec spec-strength">42% vol</div>
    <div class="spec spec-volume">70 cl</div>
  </main>
</body>
</html>
```